non prof needs power point design template

The Calloway Trust is a non profit financing and services organization. We are looking for creative ppt templates for various presentations. Including general org overview. marketing and ad decks, etc... Please utilize logo for inspiration for template. We like to communicate to our partners that we are a "business evolved" to served social causes and the public good.
We are launching next year. As such we do not have any other materials. I''m hoping you can provide a creative feel. Yes we''d like a cover page. Several slide templates for different content. Bullet points, graphs, charts, maps, statistics, combos, org charts, flow charts etc...
we work in the following sectors Agriculture and Food Accessibility, Energy, Education, Healthcare, Water/Waste Management, Housing, Emergency Services, Transportation Infrastructure, and Innovative Technologies.
Each relating to economic, food, health, environmental, personal, community, and political security.
Hope that helps.
Non Profit

```html
<!DOCTYPE html>
<html lang="en">
<head>
<meta charset="utf-8">
<title>The Calloway Trust – Presentation Template</title>
<link rel="stylesheet" href="https://fonts.googleapis.com/css2?family=Open+Sans:ital,wght@0,300;0,400;0,600;0,700;1,400&family=Open+Sans+Condensed:wght@700&display=swap">
<style>
:root{
  --bg:#d4d5d7;
  --paper:#ffffff;
  --green:#7a9e3f;
  --green-light:#a9c47a;
  --blue:#2a7dc4;
  --grey-dark:#555759;
  --grey:#8a8c8e;
  --grey-bar:#c9cacb;
  --text:#5a5c5e;
}
*{margin:0;padding:0;box-sizing:border-box}
html,body{width:1200px;height:896px;overflow:hidden;background:var(--bg);font-family:"Open Sans",Arial,sans-serif;color:var(--text)}
.canvas{position:relative;width:1200px;height:896px}
.slide{position:absolute;width:357px;height:276px;background:var(--paper);overflow:hidden}
.slide::after{content:"";position:absolute;left:0;right:0;bottom:0;height:6px;background:var(--green)}
.page-no{position:absolute;right:4px;bottom:0;font-size:4px;color:#fff;z-index:2;line-height:6px}
.col-1{left:58px}.col-2{left:430px}.col-3{left:803px}
.row-1{top:14px}.row-2{top:302px}.row-3{top:592px}
.abs{position:absolute}
.slide-title{position:absolute;left:23px;top:14px;width:313px;font-weight:300;font-size:13px;color:var(--green);border-bottom:1px solid #b8b9bb;padding-bottom:1px;letter-spacing:-.2px}
.footer-brand{position:absolute;left:11px;bottom:14px;display:flex;align-items:center;gap:3px;font-size:7px;color:var(--grey-dark);font-weight:600}
.footer-brand .dot{width:6px;height:6px;background:var(--blue)}
.photo{position:absolute}
/* cover */
.cover-panel{left:5px;top:5px;width:347px;height:157px;background:linear-gradient(100deg,#b5cc8c 0%,#93b25d 45%,#7a9e3f 100%)}
.cover-rule{left:5px;top:164px;width:347px;height:3px;background:var(--grey-dark)}
.cover-welcome{right:30px;top:80px;font-family:"Open Sans Condensed","Arial Narrow",sans-serif;font-weight:700;font-size:22px;color:#fff}
.cover-sub{right:30px;top:108px;font-size:10.5px;letter-spacing:2.6px;color:#fff;font-weight:300}
.cover-date{right:30px;top:126px;font-size:7px;color:#fff}
.cover-brand{left:190px;top:212px;display:flex;align-items:center;gap:7px;font-size:15px;color:var(--grey-dark);font-weight:600}
.cover-brand .dot{width:14px;height:14px;background:var(--blue)}
/* agenda */
.agenda-item{position:absolute;left:68px;height:20px;width:226px}
.agenda-num{position:absolute;left:0;top:-1px;width:21px;height:21px;border-radius:50%;background:var(--blue);border:2px solid #fff;box-shadow:0 0 0 1px #d0d0d0;color:#fff;font-size:10px;text-align:center;line-height:17px;z-index:1}
.agenda-bar{position:absolute;left:16px;top:0;right:0;height:20px;background:var(--grey-bar);font-size:9.6px;color:var(--grey-dark);padding-left:21px;line-height:20px}
/* text */
.label-green{font-size:5.4px;line-height:9.6px;color:var(--green);text-transform:uppercase}
.body-small{font-size:5.3px;line-height:9.6px;color:var(--text);text-align:justify}
.body-small p+p{margin-top:9px}
.body-tiny{font-size:4.6px;line-height:7.2px;color:var(--text);text-align:justify}
.body-tiny p+p{margin-top:7px}
.blue-band{left:0;top:59px;width:357px;height:67px;background:var(--blue)}
.band-quote{left:150px;top:74px;width:180px;font-style:italic;font-size:6.2px;line-height:12.6px;color:#fff;text-align:justify}
.bullet-head{font-size:7.4px;color:var(--blue)}
.bullet-list{list-style:none;font-size:6.1px;color:var(--grey)}
.bullet-list li{margin-top:6.2px;white-space:nowrap}
.bullet-list li::before{content:"▪ ";color:var(--blue)}
.mission-rule{left:132px;top:70px;width:1px;height:160px;background:var(--green-light)}
.mission-lead{left:18px;top:116px;width:110px;text-align:center;font-size:5.6px;line-height:9.6px;color:var(--blue);text-transform:uppercase}
/* charts */
.legend-key{font-size:7px;color:var(--blue)}
.legend-key::before{content:"";display:inline-block;width:4px;height:4px;background:var(--blue);margin-right:5px;vertical-align:1px}
.legend-key.grey{color:var(--grey-dark)}
.legend-key.grey::before{background:var(--grey-dark)}
.legend-text{margin-left:10px;margin-top:2px;font-size:5px;line-height:6.8px;color:var(--text);width:110px}
.chart-legend{font-size:5px;color:var(--green)}
.chart-legend .sw{display:inline-block;width:5px;height:5px;vertical-align:-0.5px;margin-right:2px}
.chart-legend p{margin-top:2px;font-size:3.6px;line-height:4.8px;color:var(--grey);width:74px;text-align:justify}
/* table */
.invest-table{left:40px;top:62px;width:288px;border-collapse:collapse;font-size:6.1px;color:#222;border:1px solid #c7c7c7}
.invest-table caption{background:var(--blue);color:#fff;font-weight:700;font-size:8.4px;text-align:left;padding:3px 6px;height:18px;caption-side:top}
.invest-table td{height:11.6px;padding:0 3px;border-bottom:1px solid #d9d9d9;border-left:1px solid #d9d9d9}
.invest-table td.num{text-align:right}
.invest-table tr:nth-child(even) td{background:#f5f5f5}
.invest-table tr.total td{font-weight:700;height:14px;border-top:1px solid #999;background:#fff}
</style>
</head>
<body>
<div class="canvas">

  <section class="slide col-1 row-1">
    <div class="abs cover-panel"></div>
    <div class="abs cover-rule"></div>
    <div class="abs cover-welcome">WELCOME</div>
    <div class="abs cover-sub">TO OUR PRESENTATION</div>
    <div class="abs cover-date">Birmingham, March 25, 2015</div>
    <div class="abs cover-brand"><span class="dot"></span>The Calloway Trust</div>
  </section>

  <section class="slide col-2 row-1">
    <h2 class="slide-title">AGENDA</h2>
    <div class="agenda-item" style="top:92px"><span class="agenda-num">1</span><div class="agenda-bar">LOREM IPSUM DOLOR SIT MET</div></div>
    <div class="agenda-item" style="top:120px"><span class="agenda-num">2</span><div class="agenda-bar">LOREM IPSUM DOLOR SIT MET</div></div>
    <div class="agenda-item" style="top:148px"><span class="agenda-num">3</span><div class="agenda-bar">LOREM IPSUM DOLOR SIT MET</div></div>
    <div class="agenda-item" style="top:176px"><span class="agenda-num">4</span><div class="agenda-bar">LOREM IPSUM DOLOR SIT MET</div></div>
    <div class="agenda-item" style="top:204px"><span class="agenda-num">5</span><div class="agenda-bar">LOREM IPSUM DOLOR SIT MET</div></div>
    <div class="footer-brand"><span class="dot"></span>Calloway Trust</div>
    <span class="page-no">2</span>
  </section>

  <section class="slide col-3 row-1">
    <h2 class="slide-title">ABOUT US</h2>
    <div class="photo" role="img" aria-label="Photo of volunteers standing together in a green park" style="left:23px;top:41px;width:312px;height:76px;background:linear-gradient(90deg,#5e8a3a,#86a95a 40%,#4f6f86 70%,#6f9a4a)"></div>
    <div class="abs label-green" style="left:23px;top:132px;width:92px">Lorem ipsum dolor sit met consectetur adipiscing elit, sed do euismod tempor incididunt ut labore et delore magna</div>
    <div class="abs body-small" style="left:146px;top:132px;width:190px">
      <p>Lorem ipsum dolor sit amet, consectetur adipiscing elit, sed do eiusmod tempor incididunt ut labore et dolore magna aliqua. Ut enim ad minim veniam, quis nostrud exercitation ullamco laboris nisi ut aliquip ex ea commodo consequat. Duis aute irure dolor in reprehenderit in voluptate velit esse cillum dolore eu fugiat nulla pariatur.</p>
      <p>Lorem ipsum dolor sit amet, consectetur adipiscing elit, sed do eiusmod tempor incididunt ut labore et dolore magna aliqua. Ut enim ad minim veniam, quis nostrud exercitation ullamco laboris nisi ut aliquip ex ea commodo consequat. Duis aute irure dolor in reprehenderit in voluptate velit esse cillum dolore eu</p>
    </div>
    <div class="footer-brand"><span class="dot"></span>Calloway Trust</div>
    <span class="page-no">2</span>
  </section>

  <section class="slide col-1 row-2">
    <h2 class="slide-title">ABOUT US</h2>
    <div class="abs blue-band"></div>
    <div class="photo" role="img" aria-label="Photo of a group of people gathered around a table signing papers outdoors" style="left:22px;top:50px;width:120px;height:79px;background:linear-gradient(120deg,#c9c2b4,#8a7a6a 50%,#4e4a48)"></div>
    <div class="abs band-quote">Lorem ipsum dolor sit amet<br>consectetur adipiscing elit, sed do eiusmod tempor incididunt ut labore et dolore magna aliqua. Ut enim ad</div>
    <div class="abs body-tiny" style="left:150px;top:134px;width:180px">
      <p>Lorem ipsum dolor sit amet, consectetur adipiscing elit, sed do eiusmod tempor incididunt ut labore et dolore magna aliqua. Ut enim ad minim veniam, quis nostrud exercitation ullamco laboris nisi ut aliquip ex ea commodo consequat. Duis aute irure dolor in reprehenderit in voluptate velit esse cillum dolore eu fugiat nulla pariatur.</p>
      <p>Lorem ipsum dolor sit amet, consectetur adipiscing elit, sed do eiusmod tempor incididunt ut labore et dolore magna aliqua. Ut enim ad minim veniam, quis nostrud exercitation ullamco laboris nisi ut aliquip ex ea commodo consequat. Duis aute irure dolor in reprehenderit in voluptate velit esse cillum dolore eu</p>
      <p>fugiat nulla pariatur. Excepteur sint occaecat cupidatat non proident, sunt in culpa qui officia deserunt mollit anim id est laborum. Excepteur sint occaecat cupidatat non proident, sunt in consequat. Duis aute irure dolor in reprehenderit</p>
    </div>
    <div class="footer-brand"><span class="dot"></span>Calloway Trust</div>
    <span class="page-no">2</span>
  </section>

  <section class="slide col-2 row-2">
    <h2 class="slide-title">BULLET TEXT</h2>
    <div class="abs" style="left:40px;top:74px">
      <div class="bullet-head">1. Lorem ipsum dolor sit amet</div>
      <ul class="bullet-list" style="margin-left:9px">
        <li>Lorem ipsum dolor sit amet, consectetur adipiscing elit, sed do eiusmod tempor incididunt ut</li>
        <li>labore et dolore magna aliqua. Ut enim ad minim veniam, quis nostrud exercitation ullamco</li>
        <li>laboris nisi ut aliquip ex ea commodo consequat. Duis aute irure dolor in reprehenderit in</li>
      </ul>
    </div>
    <div class="abs" style="left:40px;top:145px">
      <div class="bullet-head">2. Lorem ipsum dolor sit amet</div>
      <ul class="bullet-list" style="margin-left:9px">
        <li>Lorem ipsum dolor sit amet, consectetur adipiscing elit, sed do eiusmod tempor incididunt ut</li>
        <li>labore et dolore magna aliqua. Ut enim ad minim veniam, quis nostrud exercitation ullamco</li>
        <li>laboris nisi ut aliquip ex ea commodo consequat. Duis aute irure dolor in reprehenderit in</li>
      </ul>
    </div>
    <div class="footer-brand"><span class="dot"></span>Calloway Trust</div>
    <span class="page-no">2</span>
  </section>

  <section class="slide col-3 row-2">
    <h2 class="slide-title">OUR MISSION</h2>
    <div class="abs mission-rule"></div>
    <div class="abs mission-lead">Lorem ipsum dolor sit met consectetur adipiscing elit, sed do euismod tempor incididunt ut labore et delore magna</div>
    <div class="abs body-small" style="left:146px;top:90px;width:190px;font-size:5.9px;line-height:9.4px">
      <p>Lorem ipsum dolor sit amet, consectetur adipiscing elit, sed do eiusmod tempor incididunt ut labore et dolore magna aliqua. Ut enim ad minim veniam, quis nostrud exercitation ullamco laboris nisi ut aliquip ex ea commodo consequat. Duis aute irure dolor in reprehenderit in voluptate velit esse cillum dolore eu fugiat nulla pariatur.</p>
      <p>Lorem ipsum dolor sit amet, consectetur adipiscing elit, sed do eiusmod tempor incididunt ut labore et dolore magna aliqua. Ut enim ad minim veniam, quis nostrud exercitation ullamco laboris nisi ut aliquip ex ea commodo consequat. Duis aute irure dolor in reprehenderit in voluptate velit esse cillum dolore eu</p>
    </div>
    <div class="footer-brand"><span class="dot"></span>Calloway Trust</div>
    <span class="page-no">2</span>
  </section>

  <section class="slide col-1 row-3">
    <h2 class="slide-title">OUR CHART</h2>
    <div class="abs" style="left:26px;top:48px">
      <div class="legend-key">60%</div>
      <p class="legend-text">dolor sit amet, consectetur adipiscing elit, sed do eiusmod tempor incididunt ut labore et dolore magna aliqua. Ut enim ad minim veniam, quis nostrud exercitation ullamco laboris nisi ut aliquip ex ea cesse cillum dolore eu fugiat nulla pariatur.</p>
    </div>
    <div class="abs" style="left:26px;top:113px">
      <div class="legend-key">25%</div>
      <p class="legend-text">dolor sit amet, consectetur adipiscing elit, sed do eiusmod tempor incididunt ut labore et dolore magna aliqua. Ut enim ad minim veniam, quis nostrud exercitation ullamco laboris nisi ut aliquip ex ea cesse cillum dolore eu fugiat nulla pariatur.</p>
    </div>
    <div class="abs" style="left:26px;top:174px">
      <div class="legend-key grey">15%</div>
      <p class="legend-text">dolor sit amet, consectetur adipiscing elit, sed do eiusmod tempor incididunt ut labore et dolore magna aliqua. Ut enim ad minim veniam, quis nostrud exercitation ullamco laboris nisi ut aliquip ex ea cesse cillum dolore eu fugiat nulla pariatur.</p>
    </div>
    <div class="abs" style="left:190px;top:47px;width:138px;text-align:right;font-size:7.4px;color:var(--blue)">Lorem ipsum dolor sit amet</div>
    <div class="abs" style="left:190px;top:61px;width:138px;text-align:center;font-size:4.6px;line-height:6.6px;color:var(--text)">Lorem ipsum dolor sit amet, consectetur adipiscing elit, sed do eiusmod tempor incididunt ut labore et dolore magna aliqua. Ut enim ad minim veniam, quis nostrud exercitation ullamco laboris nisi ut aliquip ex ea commodo consequat. Duis aute irure dolor in reprehenderit in voluptate velit esse cillum dolore eu fugiat nulla pariatur.</div>
    <svg class="abs" style="left:0;top:0" width="357" height="276" viewBox="0 0 357 276">
      <path d="M242 182 L242 128 A54 54 0 0 1 285.7 150.3 Z" fill="#555759"/>
      <path d="M242 182 L285.7 150.3 A54 54 0 0 1 273.7 225.7 Z" fill="#2a7dc4"/>
      <path d="M242 182 L273.7 225.7 A54 54 0 1 1 242 128 Z" fill="#7a9e3f"/>
      <g font-family="Open Sans, Arial, sans-serif" font-size="7" fill="#fff">
        <text x="248" y="152">15%</text>
        <text x="266" y="187">25%</text>
        <text x="206" y="187">60%</text>
      </g>
    </svg>
    <div class="footer-brand"><span class="dot"></span>Calloway Trust</div>
    <span class="page-no">2</span>
  </section>

  <section class="slide col-2 row-3">
    <h2 class="slide-title">OUR CHART</h2>
    <svg class="abs" style="left:0;top:0" width="357" height="276" viewBox="0 0 357 276">
      <g stroke="#555759" stroke-width="0.8">
        <line x1="72" y1="48" x2="72" y2="172"/>
        <line x1="72" y1="172" x2="278" y2="172"/>
        <line x1="69" y1="48" x2="72" y2="48"/><line x1="69" y1="72" x2="72" y2="72"/>
        <line x1="69" y1="97" x2="72" y2="97"/><line x1="69" y1="122" x2="72" y2="122"/>
        <line x1="69" y1="147" x2="72" y2="147"/><line x1="69" y1="172" x2="72" y2="172"/>
      </g>
      <g fill="#7a9e3f">
        <rect x="82" y="82" width="12" height="90"/><rect x="134" y="106" width="12" height="66"/>
        <rect x="188" y="90" width="12" height="82"/><rect x="241" y="93" width="12" height="79"/>
      </g>
      <g fill="#555759">
        <rect x="94" y="122" width="12" height="50"/><rect x="146" y="82" width="12" height="90"/>
        <rect x="200" y="132" width="12" height="40"/><rect x="253" y="122" width="12" height="50"/>
      </g>
      <g fill="#2a7dc4">
        <rect x="106" y="130" width="12" height="42"/><rect x="158" y="130" width="12" height="42"/>
        <rect x="212" y="114" width="12" height="58"/><rect x="265" y="85" width="12" height="87"/>
      </g>
      <g font-family="Open Sans, Arial, sans-serif" font-size="9" fill="#7a9e3f" font-weight="300">
        <text x="90" y="190">2009</text><text x="143" y="190">2010</text>
        <text x="196" y="190">2011</text><text x="249" y="190">2012</text>
      </g>
    </svg>
    <div class="abs chart-legend" style="left:54px;top:205px"><span class="sw" style="background:var(--green)"></span>LOREM IPSUM<p>Lorem ipsum dolor sit amet, consectetur adipiscing elit, sed do eiusmod tempor incididunt ut labore et dolore magna</p></div>
    <div class="abs chart-legend" style="left:154px;top:205px;color:var(--grey-dark)"><span class="sw" style="background:var(--grey-dark)"></span>LOREM IPSUM<p>Lorem ipsum dolor sit amet, consectetur adipiscing elit, sed do eiusmod tempor incididunt ut labore et dolore magna</p></div>
    <div class="abs chart-legend" style="left:250px;top:205px;color:var(--blue)"><span class="sw" style="background:var(--blue)"></span>LOREM IPSUM<p>Lorem ipsum dolor sit amet, consectetur adipiscing elit, sed do eiusmod tempor incididunt ut labore et dolore magna</p></div>
    <div class="footer-brand"><span class="dot"></span>Calloway Trust</div>
    <span class="page-no">2</span>
  </section>

  <section class="slide col-3 row-3">
    <h2 class="slide-title">OUR TABLE</h2>
    <table class="abs invest-table">
      <caption>Growth &amp; Income Investments</caption>
      <colgroup><col style="width:130px"><col style="width:46px"><col style="width:36px"><col style="width:10px"><col></colgroup>
      <tr><td>Stillwater Partners</td><td>Marion</td><td>IRA</td><td>$</td><td class="num">176,445.44</td></tr>
      <tr><td>Northgate Asset Management</td><td>Trust</td><td>NQ</td><td>$</td><td class="num">211,914.52</td></tr>
      <tr><td>Anchor Portfolio</td><td>Trust</td><td>NQ</td><td>$</td><td class="num">177,033.59</td></tr>
      <tr><td>Meridian Health Trust</td><td>Dale</td><td>IRA</td><td>$</td><td class="num">269,724.35</td></tr>
      <tr><td>Birchwood Fund</td><td>Dale</td><td>IRA</td><td>$</td><td class="num">37,766.03</td></tr>
      <tr><td>Larkspur</td><td>Dale</td><td>IRA</td><td>$</td><td class="num">47,684.15</td></tr>
      <tr><td>Larkspur</td><td>Marion</td><td>IRA</td><td>$</td><td class="num">10,745.27</td></tr>
      <tr><td>Fenwick Realty</td><td>Dale</td><td>IRA</td><td>$</td><td class="num">77,123.47</td></tr>
      <tr><td>Summit Ridge Capital</td><td>Dale</td><td>IRA</td><td>$</td><td class="num">58,843.79</td></tr>
      <tr><td>Summit Ridge Capital</td><td>Marion</td><td>IRA</td><td>$</td><td class="num">80,283.22</td></tr>
      <tr class="total"><td colspan="3">Total Growth &amp; Income Investments</td><td>$</td><td class="num">1,147,563.83</td></tr>
    </table>
    <div class="abs" style="left:42px;top:219px;width:290px;font-size:5.6px;line-height:8.6px;color:var(--text)">Lorem ipsum dolor sit amet, consectetur adipiscing elit, sed do eiusmod tempor incididunt ut labore et dolore magna aliqua. Ut enim ad minim veniam, quis nostrud exercitation ullamco laboris nisi ut aliquip ex</div>
    <div class="footer-brand"><span class="dot"></span>Calloway Trust</div>
    <span class="page-no">2</span>
  </section>

</div>
</body>
</html>
```